Shopify store for hemp

I need a store designed for Shopify for my hemp company. I currently have a brick and mortar store, but we are looking to get some business online as well. I will upload our logo for reference. We want a clean look. Categories like THCA Flower, Concentrates, Vapes, Edibles would be nice so that we can put individual products under them. I want something about all products being third-party lab tested. All products are sourced in the United States.
Updates

Target Market(s)

Former customers who live in different areas and signed up for our marketing list.

Industry/Entity Type

Hemp/Cannabis

Coding

Coded - Design and coding required

Number of Pages Required

1 page

Requirements
Must have
• Clean feel

```html
<!DOCTYPE html>
<html lang="en">
<head>
<meta charset="utf-8">
<title>Ridgeline Hemp – Premium Hemp Products</title>
<link href="https://fonts.googleapis.com/css2?family=Bitter:wght@600;700;800&family=Poppins:ital,wght@0,400;0,500;0,600;1,400&display=swap" rel="stylesheet">
<style>
:root{
  --green:#3f9a5c;
  --green-dark:#2f6b46;
  --forest:#1f5a2c;
  --ink:#1d1d1d;
  --muted:#7a7a7a;
  --line:#e2e2e2;
  --soft:#e9ece7;
  --footer:#eef0ec;
  --sale:#e8a23a;
  --star:#f3b51c;
  --white:#ffffff;
}
*{box-sizing:border-box;margin:0;padding:0}
html,body{width:1200px;height:3752px;overflow:hidden}
body{font-family:"Poppins",sans-serif;color:var(--ink);background:var(--white);position:relative}
.slab{font-family:"Bitter",serif}
.abs{position:absolute}

/* top bar & header */
.topbar{position:absolute;top:0;left:0;width:1200px;height:25px;background:#0c0c0c;color:#fff;font-size:11px;text-align:center;line-height:25px}
.topbar b{font-weight:600}
.header{position:absolute;top:25px;left:0;width:1200px;height:58px;background:#fff;border-bottom:1px solid var(--line)}
.brand{position:absolute;left:127px;top:4px;display:flex;align-items:center;gap:10px;z-index:3}
.brand-mark{width:72px;height:72px;border-radius:50%;background:var(--green);border:3px solid #fff;box-shadow:0 2px 6px rgba(0,0,0,.15)}
.brand-name{font-family:"Bitter",serif;font-weight:700;font-size:15px;color:var(--forest)}
.nav{position:absolute;left:432px;top:0;height:58px;display:flex;align-items:center;gap:40px;font-size:14px}
.nav a{color:var(--ink);text-decoration:none}
.tools{position:absolute;right:102px;top:15px;display:flex;gap:16px}
.tool{width:29px;height:29px;border-radius:50%;background:#f0f0f0;display:flex;align-items:center;justify-content:center;position:relative}
.tool .badge{position:absolute;top:-4px;right:-2px;width:9px;height:9px;border-radius:50%;background:var(--green)}

/* hero */
.hero{position:absolute;top:83px;left:0;width:1200px;height:459px;background:linear-gradient(90deg,#24170f 0%,#3d2a1c 35%,#5a4630 65%,#3a3a28 100%)}
.hero-photo{position:absolute;inset:0;background:radial-gradient(ellipse at 75% 40%,rgba(120,140,80,.55),transparent 55%),radial-gradient(ellipse at 45% 75%,rgba(150,40,50,.45),transparent 45%)}
.hero h1{position:absolute;left:127px;top:140px;font-family:"Bitter",serif;font-weight:700;font-size:46px;line-height:60px;letter-spacing:3px;color:#fff}
.hero p{position:absolute;left:127px;top:257px;font-size:15px;color:#fff}
.btn-shop{position:absolute;left:127px;top:320px;width:135px;height:40px;border-radius:20px;background:var(--green);color:#fff;font-size:13px;font-weight:600;display:flex;align-items:center;justify-content:center}

/* section titles */
.sec-title{position:absolute;left:127px;font-family:"Bitter",serif;font-weight:700;font-size:27px;letter-spacing:2px}

/* product cards */
.card{position:absolute;width:221px;height:350px;border:1px solid var(--line);border-radius:8px;background:#fff}
.card.featured{box-shadow:0 6px 18px rgba(0,0,0,.12);border-color:#eee}
.tag{position:absolute;left:12px;top:10px;font-family:"Bitter",serif;font-weight:700;font-size:11px;letter-spacing:1px;color:var(--green)}
.tag.sale{color:var(--sale)}
.pimg{position:absolute;left:30px;top:50px;width:160px;height:150px;border-radius:50%}
.p-flower{background:radial-gradient(circle,#7d9a3d 0%,#5d7a2e 45%,rgba(255,255,255,0) 70%)}
.p-resin{background:radial-gradient(circle,#f0a82a 0%,#d98a12 45%,rgba(255,255,255,0) 70%)}
.p-vape{background:linear-gradient(135deg,rgba(255,255,255,0) 25%,#4ab2ef 40%,#a77ee0 60%,rgba(255,255,255,0) 75%)}
.p-gummy{background:radial-gradient(circle at 50% 40%,#6f7e40 0%,#3f8f3a 45%,rgba(255,255,255,0) 70%)}
.pname{position:absolute;left:0;right:0;top:233px;text-align:center;font-family:"Bitter",serif;font-weight:700;font-size:11px;letter-spacing:.8px}
.stars{position:absolute;left:0;right:0;top:249px;text-align:center;font-size:13px;color:var(--star);letter-spacing:1px}
.stars span{color:var(--muted);font-size:10px;margin-left:4px;letter-spacing:0}
.price{position:absolute;left:0;right:0;top:271px;text-align:center;font-size:12px;font-weight:500;color:var(--green-dark)}
.price s{font-size:8px;color:var(--muted)}
.btn-cart{position:absolute;left:32px;top:299px;width:166px;height:34px;border-radius:17px;background:#f1f1f1;color:var(--green);font-size:13px;display:flex;align-items:center;justify-content:center;gap:7px}
.featured .btn-cart{background:var(--green);color:#fff}
.arrow{position:absolute;width:32px;height:32px;border-radius:50%;display:flex;align-items:center;justify-content:center}
.arrow.prev{background:#fff;border:1px solid #cfcfcf}
.arrow.next{background:var(--green)}

/* categories */
.categories{position:absolute;top:1067px;left:0;width:1200px;height:658px;background:var(--soft)}
.tile{position:absolute;width:301px;height:223px;border-radius:3px;overflow:hidden}
.tile .icon{position:absolute;left:130px;top:128px;width:38px;height:38px;border-radius:50%;background:#fff;display:flex;align-items:center;justify-content:center}
.tile .label{position:absolute;left:0;right:0;top:178px;text-align:center;font-family:"Bitter",serif;font-weight:700;font-size:18px;letter-spacing:1px;color:#fff;text-shadow:0 1px 3px rgba(0,0,0,.5)}
.t-flower{background:linear-gradient(135deg,#c86b1e,#2f6a3a 50%,#d78a2a)}
.t-conc{background:linear-gradient(135deg,#2e4a22,#7a5a2a 50%,#1e3a1c)}
.t-vape{background:linear-gradient(90deg,#d24b3c,#e6b23a 25%,#2aa0c8 50%,#8a3ab0 75%,#c2307a)}
.t-edible{background:linear-gradient(135deg,#3a2318,#5a3a28 50%,#2a1a12)}
.t-preroll{background:linear-gradient(135deg,#2a3a22,#8a9a78 50%,#3a2a1a)}
.t-tinct{background:linear-gradient(135deg,#4a4a3a,#7a6a52 50%,#2e2e22)}

/* trust band */
.trust{position:absolute;top:1725px;left:0;width:1200px;height:146px;background:linear-gradient(180deg,#1d5a2a,#2c7a38 55%,#1f5a26)}
.trust-item{position:absolute;top:42px;display:flex;align-items:center;gap:16px;color:#fff;font-family:"Bitter",serif;font-weight:700;font-size:15px;letter-spacing:.8px;line-height:20px}
.trust-ic{width:56px;height:56px;border-radius:50%;background:#fff;display:flex;align-items:center;justify-content:center}

/* testimonials */
.reviews{position:absolute;top:2801px;left:0;width:1200px;height:446px;background:radial-gradient(ellipse at 70% 30%,#3fb04a,#1f7a2c 55%,#14541e);overflow:hidden}
.reviews h2{position:absolute;left:0;right:0;top:60px;text-align:center;font-family:"Bitter",serif;font-weight:700;font-size:27px;letter-spacing:2px;color:#fff}
.reviews .lead{position:absolute;left:0;right:0;top:108px;text-align:center;font-size:14px;color:#fff}
.rcard{position:absolute;top:153px;width:319px;height:201px;background:#fff;border-radius:6px;padding:22px 20px}
.rcard .rstars{color:var(--star);font-size:17px;letter-spacing:3px}
.rcard .quote{position:absolute;right:14px;top:16px;font-family:"Bitter",serif;font-weight:800;font-size:58px;line-height:50px;color:var(--green)}
.rcard p{margin-top:12px;font-size:13px;font-style:italic;color:#666;line-height:20px}
.who{position:absolute;left:20px;top:150px;display:flex;align-items:center;gap:10px}
.avatar{width:34px;height:34px;border-radius:50%;background:#c9a58e}
.who b{display:block;font-size:13px;font-weight:600;color:#333}
.who span{font-size:11px;color:var(--muted)}
.dots{position:absolute;top:388px;left:0;right:0;display:flex;justify-content:center;align-items:center;gap:8px}
.dots i{width:7px;height:7px;border-radius:50%;background:#ddd;display:block}
.dots i.on{width:11px;height:11px;background:transparent;border:2px solid #fff}

/* footer */
.footer{position:absolute;top:3247px;left:0;width:1200px;height:505px;background:var(--footer)}
.f-logo{position:absolute;left:116px;top:60px;width:98px;height:98px;border-radius:50%;background:var(--green)}
.f-name{position:absolute;left:106px;top:170px;font-family:"Bitter",serif;font-weight:700;font-size:15px;color:var(--forest)}
.socials{position:absolute;left:109px;top:210px;display:flex;gap:12px}
.socials i{width:23px;height:23px;border-radius:50%;border:1px solid #cfd3cc;background:#fff;display:block}
.fcol{position:absolute;top:70px}
.fcol h4{font-family:"Bitter",serif;font-weight:600;font-size:15px;margin-bottom:26px}
.fcol a{display:block;font-size:13px;color:#444;text-decoration:none;margin-bottom:12px}
.contact-row{display:flex;align-items:center;gap:10px;font-size:13px;color:#444;margin-bottom:11px}
.contact-row .ci{width:26px;height:26px;border-radius:50%;background:#fff;display:flex;align-items:center;justify-content:center}
.f-rule{position:absolute;left:109px;width:982px;height:1px;background:#d8dcd4}
.newsletter h3{position:absolute;left:109px;top:325px;font-family:"Bitter",serif;font-weight:600;font-size:18px}
.newsletter p.sub{position:absolute;left:109px;top:358px;width:340px;font-size:13px;color:#555;line-height:20px}
.email{position:absolute;left:663px;top:331px;width:316px;height:38px;border-radius:19px;background:#fff;border:1px solid #e2e4df;font-size:11px;color:#999;padding-left:12px;line-height:36px}
.subscribe{position:absolute;left:989px;top:331px;width:105px;height:38px;border-radius:19px;background:var(--green-dark);color:#fff;font-size:12px;font-weight:600;display:flex;align-items:center;justify-content:center}
.newsletter .note{position:absolute;left:667px;top:380px;font-size:11px;color:#666}
.copyright{position:absolute;left:0;right:0;top:458px;text-align:center;font-size:13px;color:#444}
</style>
</head>
<body>

<div class="topbar"><b>Free shipping</b> on orders over <b>$50</b> with secure</div>

<header class="header">
  <div class="brand"><div class="brand-mark"></div><span class="brand-name">Ridgeline Hemp</span></div>
  <nav class="nav"><a href="#">Home</a><a href="#">Catalog</a><a href="#">Collection</a><a href="#">Contact</a></nav>
  <div class="tools">
    <div class="tool"><svg width="13" height="13" viewBox="0 0 24 24" fill="none" stroke="#222" stroke-width="2.4"><circle cx="10" cy="10" r="7"/><path d="M15 15l6 6"/></svg></div>
    <div class="tool"><svg width="13" height="13" viewBox="0 0 24 24" fill="none" stroke="#222" stroke-width="2.4"><circle cx="12" cy="8" r="4"/><path d="M4 21c1-5 15-5 16 0"/></svg></div>
    <div class="tool"><svg width="14" height="14" viewBox="0 0 24 24" fill="none" stroke="#222" stroke-width="2.2"><path d="M2 3h3l3 12h11l2-8H7"/><circle cx="9" cy="20" r="1.5"/><circle cx="18" cy="20" r="1.5"/></svg><i class="badge"></i></div>
  </div>
</header>

<section class="hero">
  <div class="hero-photo" role="img" aria-label="Jars of hemp flower and colourful gummies on a shop counter"></div>
  <h1>PREMIUM HEMP<br>PRODUCTS</h1>
  <p>Shop THCA Flower, Concentrates, Vapes, Edibles.</p>
  <div class="btn-shop">SHOP NOW</div>
</section>

<!-- Best sellers -->
<h2 class="sec-title" style="top:603px">BEST SELLERS</h2>
<div class="arrow prev" style="left:73px;top:826px"><svg width="12" height="12" viewBox="0 0 24 24" fill="none" stroke="#222" stroke-width="3"><path d="M15 5l-7 7 7 7"/></svg></div>
<div class="arrow next" style="left:1094px;top:804px"><svg width="12" height="12" viewBox="0 0 24 24" fill="none" stroke="#fff" stroke-width="3"><path d="M9 5l7 7-7 7"/></svg></div>

<div class="card" style="left:127px;top:662px"><span class="tag">NEW</span><div class="pimg p-flower" role="img" aria-label="Hemp flower bud"></div><div class="pname">PREMIUM THCA FLOWER</div><div class="stars">★★★★★<span>(15)</span></div><div class="price">39.99 / <s>45.99</s></div><div class="btn-cart"><svg width="14" height="14" viewBox="0 0 24 24" fill="none" stroke="currentColor" stroke-width="2.2"><path d="M2 3h3l3 12h11l2-8H7"/><circle cx="9" cy="20" r="1.5"/><circle cx="18" cy="20" r="1.5"/></svg>ADD TO CART</div></div>
<div class="card" style="left:368px;top:662px"><span class="tag">NEW</span><div class="pimg p-resin" role="img" aria-label="Amber live resin concentrate"></div><div class="pname">LIVE RESIN CONCENTRATE</div><div class="stars">★★★★★<span>(15)</span></div><div class="price">39.99 / <s>45.99</s></div><div class="btn-cart"><svg width="14" height="14" viewBox="0 0 24 24" fill="none" stroke="currentColor" stroke-width="2.2"><path d="M2 3h3l3 12h11l2-8H7"/><circle cx="9" cy="20" r="1.5"/><circle cx="18" cy="20" r="1.5"/></svg>ADD TO CART</div></div>
<div class="card featured" style="left:610px;top:662px"><span class="tag sale">SALE</span><div class="pimg p-vape" role="img" aria-label="Two disposable vape pens"></div><div class="pname">DISPOSABLE VAPE PEN</div><div class="stars">★★★★★<span>(15)</span></div><div class="price">39.99 / <s>45.99</s></div><div class="btn-cart"><svg width="14" height="14" viewBox="0 0 24 24" fill="none" stroke="currentColor" stroke-width="2.2"><path d="M2 3h3l3 12h11l2-8H7"/><circle cx="9" cy="20" r="1.5"/><circle cx="18" cy="20" r="1.5"/></svg>ADD TO CART</div></div>
<div class="card" style="left:852px;top:662px"><span class="tag">NEW</span><div class="pimg p-gummy" role="img" aria-label="Green gummy topped with hemp bud"></div><div class="pname">DELTA-8 GUMMIES</div><div class="stars">★★★★★<span>(15)</span></div><div class="price">39.99 / <s>45.99</s></div><div class="btn-cart"><svg width="14" height="14" viewBox="0 0 24 24" fill="none" stroke="currentColor" stroke-width="2.2"><path d="M2 3h3l3 12h11l2-8H7"/><circle cx="9" cy="20" r="1.5"/><circle cx="18" cy="20" r="1.5"/></svg>ADD TO CART</div></div>

<!-- Categories -->
<section class="categories">
  <h2 class="sec-title" style="top:49px">SHOP BY CATEGORY</h2>
  <div class="tile t-flower" style="left:127px;top:120px" role="img" aria-label="Close-up of a hemp flower"><div class="icon"><svg width="18" height="18" viewBox="0 0 24 24" fill="none" stroke="#222" stroke-width="1.8"><path d="M5 19C5 10 11 5 20 5c0 9-5 14-14 14zM5 19l8-8"/></svg></div><div class="label">THCA FLOWER</div></div>
  <div class="tile t-conc" style="left:450px;top:120px" role="img" aria-label="Bottles of hemp concentrates"><div class="icon"><svg width="18" height="18" viewBox="0 0 24 24" fill="none" stroke="#222" stroke-width="1.8"><path d="M9 4c-3 5-5 8-5 11a5 5 0 0010 0c0-3-2-6-5-11zM16 8c-2 3-3 5-3 6a3 3 0 006 0c0-1-1-3-3-6z"/></svg></div><div class="label">CONCENTRATES</div></div>
  <div class="tile t-vape" style="left:772px;top:120px" role="img" aria-label="Colourful vape cartridges"><div class="icon"><svg width="18" height="18" viewBox="0 0 24 24" fill="none" stroke="#222" stroke-width="1.8"><path d="M3 9h12a3 3 0 10-3-3M3 14h16a3 3 0 11-3 3M3 19h8"/></svg></div><div class="label">VAPES</div></div>
  <div class="tile t-edible" style="left:127px;top:364px" role="img" aria-label="Hemp-infused chocolate bars"><div class="icon"><svg width="18" height="18" viewBox="0 0 24 24" fill="none" stroke="#222" stroke-width="1.8"><rect x="5" y="8" width="14" height="8" rx="4" transform="rotate(-45 12 12)"/></svg></div><div class="label">EDIBLES</div></div>
  <div class="tile t-preroll" style="left:450px;top:364px" role="img" aria-label="Bundle of pre-rolls"><div class="icon"><svg width="18" height="18" viewBox="0 0 24 24" fill="none" stroke="#222" stroke-width="1.8"><rect x="3" y="14" width="18" height="4"/><path d="M15 14v4M17 6c0 3 3 3 3 6"/></svg></div><div class="label">PRE-ROLLS</div></div>
  <div class="tile t-tinct" style="left:772px;top:364px" role="img" aria-label="Tincture bottles with hemp leaves"><div class="icon"><svg width="18" height="18" viewBox="0 0 24 24" fill="none" stroke="#222" stroke-width="1.8"><path d="M14 4l6 6M16 6l-9 9-2 4 4-2 9-9"/></svg></div><div class="label">TINCTURES</div></div>
</section>

<!-- Trust band -->
<section class="trust" role="img" aria-label="Green hemp field at dusk">
  <div class="trust-item" style="left:180px"><div class="trust-ic"><svg width="28" height="28" viewBox="0 0 24 24" fill="none" stroke="#2f6b46" stroke-width="1.6"><rect x="4" y="4" width="13" height="16" rx="1"/><path d="M7 9h7M7 13h4"/><circle cx="16" cy="16" r="3"/><path d="M18 18l3 3"/></svg></div><span>THIRD-PARTY LAB<br>TESTED</span></div>
  <div class="trust-item" style="left:461px"><div class="trust-ic"><svg width="28" height="28" viewBox="0 0 24 24" fill="none" stroke="#2f6b46" stroke-width="1.6"><path d="M12 2a6 6 0 016 6c0 5-6 11-6 11S6 13 6 8a6 6 0 016-6z"/><circle cx="12" cy="8" r="2"/><path d="M3 22h18"/></svg></div><span>US-SOURCED</span></div>
  <div class="trust-item" style="left:759px"><div class="trust-ic"><svg width="28" height="28" viewBox="0 0 24 24" fill="none" stroke="#2f6b46" stroke-width="1.6"><path d="M12 21V10M12 10C10 6 10 4 12 2c2 2 2 4 0 8zM12 13c-3-2-6-2-8-1 2 2 5 2 8 1zM12 13c3-2 6-2 8-1-2 2-5 2-8 1z"/></svg></div><span>PREMIUM QUALITY</span></div>
</section>

<!-- New arrivals -->
<h2 class="sec-title" style="top:1929px">NEW ARRIVALS</h2>

<div class="card" style="left:127px;top:1989px"><span class="tag">NEW</span><div class="pimg p-flower" role="img" aria-label="Hemp flower bud"></div><div class="pname">PREMIUM THCA FLOWER</div><div class="stars">★★★★★<span>(15)</span></div><div class="price">39.99 / <s>45.99</s></div><div class="btn-cart"><svg width="14" height="14" viewBox="0 0 24 24" fill="none" stroke="currentColor" stroke-width="2.2"><path d="M2 3h3l3 12h11l2-8H7"/><circle cx="9" cy="20" r="1.5"/><circle cx="18" cy="20" r="1.5"/></svg>ADD TO CART</div></div>
<div class="card" style="left:368px;top:1989px"><span class="tag">NEW</span><div class="pimg p-resin" role="img" aria-label="Amber live resin concentrate"></div><div class="pname">LIVE RESIN CONCENTRATE</div><div class="stars">★★★★★<span>(15)</span></div><div class="price">39.99 / <s>45.99</s></div><div class="btn-cart"><svg width="14" height="14" viewBox="0 0 24 24" fill="none" stroke="currentColor" stroke-width="2.2"><path d="M2 3h3l3 12h11l2-8H7"/><circle cx="9" cy="20" r="1.5"/><circle cx="18" cy="20" r="1.5"/></svg>ADD TO CART</div></div>
<div class="card featured" style="left:610px;top:1989px"><span class="tag sale">SALE</span><div class="pimg p-vape" role="img" aria-label="Two disposable vape pens"></div><div class="pname">DISPOSABLE VAPE PEN</div><div class="stars">★★★★★<span>(15)</span></div><div class="price">39.99 / <s>45.99</s></div><div class="btn-cart"><svg width="14" height="14" viewBox="0 0 24 24" fill="none" stroke="currentColor" stroke-width="2.2"><path d="M2 3h3l3 12h11l2-8H7"/><circle cx="9" cy="20" r="1.5"/><circle cx="18" cy="20" r="1.5"/></svg>ADD TO CART</div></div>
<div class="card" style="left:852px;top:1989px"><span class="tag">NEW</span><div class="pimg p-gummy" role="img" aria-label="Green gummy topped with hemp bud"></div><div class="pname">DELTA-8 GUMMIES</div><div class="stars">★★★★★<span>(15)</span></div><div class="price">39.99 / <s>45.99</s></div><div class="btn-cart"><svg width="14" height="14" viewBox="0 0 24 24" fill="none" stroke="currentColor" stroke-width="2.2"><path d="M2 3h3l3 12h11l2-8H7"/><circle cx="9" cy="20" r="1.5"/><circle cx="18" cy="20" r="1.5"/></svg>ADD TO CART</div></div>

<div class="card" style="left:127px;top:2360px"><span class="tag sale">SALE</span><div class="pimg p-vape" role="img" aria-label="Two disposable vape pens"></div><div class="pname">DISPOSABLE VAPE PEN</div><div class="stars">★★★★★<span>(15)</span></div><div class="price">39.99 / <s>45.99</s></div><div class="btn-cart"><svg width="14" height="14" viewBox="0 0 24 24" fill="none" stroke="currentColor" stroke-width="2.2"><path d="M2 3h3l3 12h11l2-8H7"/><circle cx="9" cy="20" r="1.5"/><circle cx="18" cy="20" r="1.5"/></svg>ADD TO CART</div></div>
<div class="card" style="left:368px;top:2360px"><span class="tag">NEW</span><div class="pimg p-flower" role="img" aria-label="Hemp flower bud"></div><div class="pname">PREMIUM THCA FLOWER</div><div class="stars">★★★★★<span>(15)</span></div><div class="price">39.99 / <s>45.99</s></div><div class="btn-cart"><svg width="14" height="14" viewBox="0 0 24 24" fill="none" stroke="currentColor" stroke-width="2.2"><path d="M2 3h3l3 12h11l2-8H7"/><circle cx="9" cy="20" r="1.5"/><circle cx="18" cy="20" r="1.5"/></svg>ADD TO CART</div></div>
<div class="card" style="left:610px;top:2360px"><span class="tag">NEW</span><div class="pimg p-gummy" role="img" aria-label="Green gummy topped with hemp bud"></div><div class="pname">DELTA-8 GUMMIES</div><div class="stars">★★★★★<span>(15)</span></div><div class="price">39.99 / <s>45.99</s></div><div class="btn-cart"><svg width="14" height="14" viewBox="0 0 24 24" fill="none" stroke="currentColor" stroke-width="2.2"><path d="M2 3h3l3 12h11l2-8H7"/><circle cx="9" cy="20" r="1.5"/><circle cx="18" cy="20" r="1.5"/></svg>ADD TO CART</div></div>
<div class="card" style="left:852px;top:2360px"><span class="tag">NEW</span><div class="pimg p-resin" role="img" aria-label="Amber live resin concentrate"></div><div class="pname">LIVE RESIN CONCENTRATE</div><div class="stars">★★★★★<span>(15)</span></div><div class="price">39.99 / <s>45.99</s></div><div class="btn-cart"><svg width="14" height="14" viewBox="0 0 24 24" fill="none" stroke="currentColor" stroke-width="2.2"><path d="M2 3h3l3 12h11l2-8H7"/><circle cx="9" cy="20" r="1.5"/><circle cx="18" cy="20" r="1.5"/></svg>ADD TO CART</div></div>

<!-- Testimonials -->
<section class="reviews" role="img" aria-label="Soft-focus green hemp leaves">
  <h2>WHAT OUR CLIENT SAY</h2>
  <div class="lead">Join thousands of satisfied customers who trust our premium hemp products.</div>
  <div class="rcard" style="left:77px"><div class="rstars">★★★★★</div><div class="quote">”</div><p>"The quality of their THCA flower is unmatched. I love that everything is lab tested and I can see the results. Will definitely be ordering again!"</p><div class="who"><div class="avatar"></div><div><b>Tessa Marlow</b><span>Austin, TX</span></div></div></div>
  <div class="rcard" style="left:412px"><div class="rstars">★★★★★</div><div class="quote">”</div><p>"I was really impressed with the range of strains available. The high THC content is exactly what I was looking for. Fast shipping too!"</p><div class="who"><div class="avatar"></div><div><b>Owen Hartley</b><span>San Francisco, CA</span></div></div></div>
  <div class="rcard" style="left:747px"><div class="rstars">★★★★★</div><div class="quote">”</div><p>"The customer service was fantastic! They answered all my questions and helped me choose the perfect strain. I'm very satisfied!"</p><div class="who"><div class="avatar"></div><div><b>Nadia Brooks</b><span>New York, NY</span></div></div></div>
  <div class="rcard" style="left:1082px"><div class="rstars">★★★★★</div><div class="quote">”</div><p>"This is the best shop I've visited. The atmosphere is great and the staff is so helpful. Highly recommended!"</p><div class="who"><div class="avatar"></div><div><b>Caleb Frost</b><span>Chicago, IL</span></div></div></div>
  <div class="dots"><i></i><i></i><i class="on"></i><i></i><i></i></div>
</section>

<!-- Footer -->
<footer class="footer">
  <div class="f-logo"></div>
  <div class="f-name">Ridgeline Hemp</div>
  <div class="socials"><i aria-label="Social link"></i><i aria-label="Social link"></i><i aria-label="Social link"></i><i aria-label="Social link"></i></div>

  <div class="fcol" style="left:333px">
    <h4>Contact</h4>
    <div class="contact-row"><span class="ci"><svg width="12" height="12" viewBox="0 0 24 24" fill="none" stroke="#3f9a5c" stroke-width="2"><path d="M5 3h4l2 5-3 2a11 11 0 006 6l2-3 5 2v4a2 2 0 01-2 2A17 17 0 013 5a2 2 0 012-2z"/></svg></span>+1 (555) 014-2290</div>
    <div class="contact-row"><span class="ci"><svg width="12" height="12" viewBox="0 0 24 24" fill="none" stroke="#3f9a5c" stroke-width="2"><rect x="3" y="5" width="18" height="14" rx="2"/><path d="M3 7l9 6 9-6"/></svg></span>hello@ridgelinehemp.example</div>
    <div class="contact-row"><span class="ci"><svg width="12" height="12" viewBox="0 0 24 24" fill="none" stroke="#3f9a5c" stroke-width="2"><path d="M12 2a7 7 0 017 7c0 5-7 13-7 13S5 14 5 9a7 7 0 017-7z"/><circle cx="12" cy="9" r="2.5"/></svg></span>Sunvale, CA</div>
  </div>
  <div class="fcol" style="left:587px"><h4>Shop</h4><a href="#">THCA Flower</a><a href="#">Concentrates</a><a href="#">Vapes</a><a href="#">Edibles</a><a href="#">All Products</a></div>
  <div class="fcol" style="left:750px"><h4>Company</h4><a href="#">About Us</a><a href="#">Lab Results</a><a href="#">Our Story</a><a href="#">Contact</a><a href="#">Careers</a></div>
  <div class="fcol" style="left:914px"><h4>Support</h4><a href="#">FAQ</a><a href="#">Shipping Info</a><a href="#">Returns</a><a href="#">Privacy Policy</a><a href="#">Terms of Service</a></div>

  <div class="f-rule" style="top:287px"></div>
  <div class="newsletter">
    <h3>Stay in the Loop</h3>
    <p class="sub">Subscribe for exclusive deals, new products, and hemp wellness tips.</p>
    <div class="email">Enter your email</div>
    <div class="subscribe">Subscribe</div>
    <div class="note">By subscribing, you agree to our Privacy Policy.</div>
  </div>
  <div class="f-rule" style="top:428px"></div>
  <div class="copyright">Copyright © 2025 | Ridgeline Hemp</div>
</footer>

</body>
</html>
```